Quill|Marlow & Petrie business card contest

We need a logo for an upscale boutique diversified company involved in real estate, investments, cattle, and more. Our businesses DO NOT need to be reflected in the business card nor do we want them noted. This is our logo and colors and we love our logo and colors. Our logo looks best against a black background and we like to include the firm name in our logo usage. importantly, the names Quill and Marlow are separated by | not / and we use an ampersand not the word and.
On the front of the card, we want to include:
company logo and name (Quill|Marlow & Petrie)
on the back, we would definitely include:
address, email, cell #
logo and name (smaller size than front)

The variable will be location of individual name and title (mine for example is ) - whether on the front OR on the back. interested in variations from which to choose
Dr. Owen T. Caldecott, CFA
Scientifique des Fusées Financières

we would like to use contemporary symbols for address, email address, cell # with an option for web site that we do not intend to use initially. we like two sided cards and believe this design should use four rounded corners with the standard size. we prefer thicker card stock and may look at metal.

```html
<!DOCTYPE html>
<html lang="en">
<head>
<meta charset="utf-8">
<title>Quill|Marlow &amp; Petrie — Business Card</title>
<link rel="stylesheet" href="https://fonts.googleapis.com/css2?family=Open+Sans:wght@400;600&display=swap">
<style>
  :root {
    --bg-top: #eef0f2;
    --bg-bottom: #c9cacc;
    --card-black: #111112;
    --card-white: #f2f2f2;
    --orange: #e07a1f;
    --grey-dark: #4a4a4a;
    --grey-mid: #6b6b6b;
    --grey-logo: #7a7a7a;
  }
  * { box-sizing: border-box; margin: 0; padding: 0; }
  html, body { width: 1200px; height: 1021px; overflow: hidden; }
  body {
    background: linear-gradient(160deg, var(--bg-top) 0%, #dcdde0 55%, var(--bg-bottom) 100%);
    font-family: "Open Sans", sans-serif;
    position: relative;
  }
  .card {
    position: absolute;
    width: 620px;
    height: 354px;
    border-radius: 22px;
    box-shadow: 0 10px 24px rgba(0,0,0,0.22);
  }
  .card--front {
    left: 330px; top: 130px;
    background: var(--card-black);
    display: flex; align-items: center; justify-content: center;
  }
  .card--back {
    left: 250px; top: 530px;
    background: var(--card-white);
    display: flex; align-items: center;
    padding: 0 44px 0 46px;
  }
  .firm-name {
    font-weight: 400;
    color: var(--grey-logo);
    white-space: nowrap;
    display: flex; align-items: center; gap: 14px;
  }
  .firm-name__mark {
    width: 22px; height: 22px;
    background: var(--orange);
    flex: none;
  }
  .card--front .firm-name { font-size: 38px; }
  .card--back .firm-name { font-size: 22px; color: var(--grey-dark); gap: 10px; }
  .card--back .firm-name__mark { width: 16px; height: 16px; }
  .back__brand { width: 262px; flex: none; }
  .divider {
    flex: none;
    width: 2px; height: 190px;
    margin: 0 30px 0 14px;
    background: linear-gradient(to bottom, var(--orange) 0 26%, transparent 26% 32%, var(--grey-mid) 32% 100%);
  }
  .contact { color: var(--grey-dark); font-size: 15px; line-height: 1.45; }
  .contact__name { color: var(--orange); font-weight: 600; font-size: 19px; line-height: 1.2; }
  .contact__name small { font-size: 14px; }
  .contact__title { font-size: 15px; margin-bottom: 12px; }
  .contact__address { margin-bottom: 6px; }
  .contact__row { display: flex; align-items: center; gap: 8px; }
  .contact__row svg { width: 15px; height: 15px; flex: none; }
</style>
</head>
<body>
  <section class="card card--front" aria-label="Card front">
    <div class="firm-name"><span class="firm-name__mark"></span>Quill|Marlow &amp; Petrie</div>
  </section>

  <section class="card card--back" aria-label="Card back">
    <div class="back__brand">
      <div class="firm-name"><span class="firm-name__mark"></span>Quill|Marlow &amp; Petrie</div>
    </div>
    <div class="divider"></div>
    <div class="contact">
      <p class="contact__name">Dr. Owen T. Caldecott, <small>CFA</small></p>
      <p class="contact__title">Scientifique des Fusées Financières</p>
      <p class="contact__address">48 Larkspur Row, Suite 210<br>Fernhill, Oregon, 97001</p>
      <p class="contact__row">
        <svg viewBox="0 0 16 16" fill="none" stroke="var(--orange)" stroke-width="1.4"><rect x="4" y="1.5" width="8" height="13" rx="1.5"/><line x1="7" y1="12" x2="9" y2="12"/></svg>
        (555) 014-2298
      </p>
      <p class="contact__row">
        <svg viewBox="0 0 16 16" fill="none" stroke="var(--orange)" stroke-width="1.4"><rect x="1.5" y="3.5" width="13" height="9"/><polyline points="1.5,3.5 8,9 14.5,3.5"/></svg>
        info@quillmarlowpetrie.com
      </p>
      <p class="contact__row">
        <svg viewBox="0 0 16 16" fill="none" stroke="var(--orange)" stroke-width="1.2"><circle cx="8" cy="8" r="6.5"/><ellipse cx="8" cy="8" rx="3" ry="6.5"/><line x1="1.5" y1="8" x2="14.5" y2="8"/></svg>
        www.quillmarlowpetrie.com
      </p>
    </div>
  </section>
</body>
</html>
```